Hal's Remedies Business Card Design Project

I need a business card designed for my pharmacy Hal's Remedies. I would like just the logo on one side, maybe with black background and white lettering. The other side I would also like to include my logo which is attached. Also, please include my name and the following information:
Hal Norwick Owner/Pharm D.
Business address is 7163 N Birch Rd Sioux Falls, SD 57291.
Phone number is 605-318-6027 and fax # is 605-318-6031.
my email address is hal@halsremedies.example.
My website is www.halsremedies.example.
My business hours are Monday-Friday 8am-7 pm. Saturday 8am-12 pm. Sunday Closed.
I would like the design to include my logo colors, black, white, and neon green. Silver may be added as a highlight. Thanks.
Pharmacy
See above in product description

```html
<!DOCTYPE html>
<html lang="en">
<head>
<meta charset="utf-8">
<title>Hal's Remedies – Business Card</title>
<link rel="stylesheet" href="https://fonts.googleapis.com/css2?family=Open+Sans:wght@600&family=Questrial&display=swap">
<style>
  :root {
    --ink: #050707;
    --front-bg: #000000;
    --white: #ffffff;
    --neon: #8ee000;
    --seam: #6b6b6b;
    --rule: 1.5px solid var(--white);
  }
  * { box-sizing: border-box; margin: 0; padding: 0; }
  html, body { width: 921px; height: 1200px; overflow: hidden; background: var(--ink); }
  body { position: relative; color: var(--white); font-family: "Questrial", sans-serif; }

  .card { position: absolute; left: 0; width: 921px; height: 600px; }
  .card--front { top: 0; background: var(--front-bg); border-bottom: 1px solid var(--seam); }
  .card--back { top: 600px; background: var(--ink); }

  .brand-lockup {
    position: absolute; left: 0; right: 0; top: 0; bottom: 0;
    display: flex; align-items: center; justify-content: center; gap: 26px;
  }
  .brand-dot { width: 56px; height: 56px; border-radius: 50%; background: var(--neon); flex: none; }
  .brand-name {
    font-family: "Open Sans", sans-serif; font-weight: 600;
    font-size: 62px; letter-spacing: -2px; color: var(--white); white-space: nowrap;
  }

  .cell {
    position: absolute; border: var(--rule);
    display: flex; align-items: center; justify-content: center; text-align: center;
  }
  .cell--title { left: 44px; top: 46px; width: 831px; height: 94px; }
  .cell--title .brand-name { font-size: 40px; letter-spacing: -1.4px; }
  .cell--name { left: 44px; top: 139px; width: 416px; height: 99px; font-size: 25px; letter-spacing: 0.5px; }
  .cell--role { left: 459px; top: 139px; width: 416px; height: 99px; font-size: 25px; letter-spacing: 0.5px; }
  .cell--mark { left: 44px; top: 237px; width: 291px; height: 153px; gap: 12px; }
  .cell--mark .brand-dot { width: 22px; height: 22px; }
  .cell--mark .brand-name { font-size: 26px; letter-spacing: -0.8px; }
  .cell--hours { left: 44px; top: 389px; width: 291px; height: 162px; flex-direction: column; font-size: 25px; line-height: 33px; letter-spacing: 0.4px; }
  .cell--contact {
    left: 334px; top: 237px; width: 541px; height: 314px;
    display: block; padding-top: 41px; font-size: 24px; line-height: 33px; letter-spacing: 0.4px;
  }
  .contact-group { margin-top: 34px; }
  .accent { color: var(--neon); }
</style>
</head>
<body>
  <section class="card card--front">
    <div class="brand-lockup">
      <span class="brand-dot"></span>
      <span class="brand-name">Hal's Remedies</span>
    </div>
  </section>

  <section class="card card--back">
    <div class="cell cell--title"><span class="brand-name">Hal's Remedies</span></div>
    <div class="cell cell--name">Hal Norwick</div>
    <div class="cell cell--role">Owner<span class="accent">/</span>Pharm D.</div>
    <div class="cell cell--mark">
      <span class="brand-dot"></span>
      <span class="brand-name">Hal's Remedies</span>
    </div>
    <div class="cell cell--hours">
      <p>Mo<span class="accent">-</span>Fri: 8am<span class="accent">-</span>7pm</p>
      <p>Sa: 8am<span class="accent">-</span>12pm</p>
      <p>Sunday Closed</p>
    </div>
    <div class="cell cell--contact">
      <p>7163 N Birch Rd Sioux Falls, SD 57291</p>
      <div class="contact-group">
        <p><span class="accent">T</span> 605-318-6027</p>
        <p><span class="accent">F</span> 605-318-6031</p>
      </div>
      <div class="contact-group">
        <p>hal@halsremedies.example</p>
        <p>www.halsremedies.example</p>
      </div>
    </div>
  </section>
</body>
</html>
```